Professional Services (B-2-B) Business Cards (Front & Back)

Quintarion is a business-to-business professional services company in the legal sector. They typically present to c-suite and executive functions who are looking for providers with expertise, and experience. Our business card should look and feel professional and contemporary, but we are not a startup tech company, so we want the tone to be more mature.

```html
<!DOCTYPE html>
<html lang="en">
<head>
<meta charset="UTF-8">
<title>Quintarion Business Cards</title>
<link rel="stylesheet" href="https://fonts.googleapis.com/css2?family=Oswald:wght@600&family=Montserrat:wght@400;500&display=swap">
<style>
  :root {
    --navy: #04306f;
    --accent: #0a7fd6;
    --ink: #4a4a4a;
    --paper: #ffffff;
    --backdrop: #e4e4e4;
  }
  * { margin: 0; padding: 0; box-sizing: border-box; }
  html, body { width: 1200px; height: 1200px; overflow: hidden; }
  body {
    background: var(--backdrop);
    position: relative;
    font-family: "Montserrat", sans-serif;
  }
  .card {
    position: absolute;
    left: 257px;
    width: 686px;
    height: 392px;
  }
  .card--front { top: 165px; background: var(--paper); }
  .card--back { top: 653px; background: var(--navy); }

  .brand-front {
    position: absolute;
    right: 55px;
    top: 62px;
    display: flex;
    align-items: center;
    gap: 12px;
    color: var(--navy);
    font-weight: 500;
    font-size: 30px;
    letter-spacing: 0.02em;
  }
  .brand-square {
    width: 22px;
    height: 22px;
    background: currentColor;
  }

  .holder {
    position: absolute;
    left: 46px;
    top: 225px;
  }
  .holder__name {
    font-family: "Oswald", sans-serif;
    font-weight: 600;
    font-size: 32px;
    line-height: 1;
    color: var(--navy);
    letter-spacing: 0.01em;
    text-transform: uppercase;
  }
  .holder__title {
    margin-top: 4px;
    font-size: 16px;
    color: var(--accent);
    letter-spacing: 0.02em;
  }

  .contacts {
    position: absolute;
    left: 46px;
    top: 304px;
    display: flex;
    font-size: 15.5px;
    color: var(--ink);
  }
  .contacts__col { display: flex; flex-direction: column; gap: 5px; }
  .contacts__col--phones { padding-right: 17px; border-right: 1.5px solid var(--accent); }
  .contacts__col--web { padding-left: 18px; }
  .contact { display: flex; align-items: center; gap: 8px; line-height: 17px; }
  .contact svg { width: 14px; height: 14px; flex: none; fill: var(--accent); }

  .brand-back {
    position: absolute;
    left: 0; right: 0;
    top: 176px;
    display: flex;
    justify-content: center;
    align-items: center;
    gap: 24px;
    color: #ffffff;
    font-weight: 500;
    font-size: 31px;
    letter-spacing: 0.36em;
    text-transform: uppercase;
  }
  .brand-back .brand-square { width: 28px; height: 28px; }
</style>
</head>
<body>
  <section class="card card--front" aria-label="Business card front">
    <div class="brand-front"><span class="brand-square"></span>Quintarion</div>

    <div class="holder">
      <h1 class="holder__name">Alan Mercer</h1>
      <p class="holder__title">President &amp; CEO</p>
    </div>

    <div class="contacts">
      <div class="contacts__col contacts__col--phones">
        <div class="contact">
          <svg viewBox="0 0 24 24" aria-hidden="true"><path d="M6.6 10.8a15.1 15.1 0 0 0 6.6 6.6l2.2-2.2c.3-.3.7-.4 1-.2 1.1.4 2.3.6 3.6.6.6 0 1 .4 1 1V20c0 .6-.4 1-1 1A17 17 0 0 1 3 4c0-.6.4-1 1-1h3.5c.6 0 1 .4 1 1 0 1.3.2 2.5.6 3.6.1.3 0 .7-.2 1l-2.3 2.2z"/></svg>
          <span>(415) 555-0148</span>
        </div>
        <div class="contact">
          <svg viewBox="0 0 24 24" aria-hidden="true"><path d="M7 1h10a2 2 0 0 1 2 2v18a2 2 0 0 1-2 2H7a2 2 0 0 1-2-2V3a2 2 0 0 1 2-2zm0 3v14h10V4H7zm5 15.2a1.1 1.1 0 1 0 0 2.2 1.1 1.1 0 0 0 0-2.2z"/></svg>
          <span>(203) 555-0172</span>
        </div>
      </div>
      <div class="contacts__col contacts__col--web">
        <div class="contact">
          <svg viewBox="0 0 24 24" aria-hidden="true"><path d="M2 5h20v14H2V5zm2 2v.5l8 5.5 8-5.5V7H4zm0 2.9V17h16V9.9l-8 5.5-8-5.5z"/></svg>
          <span>amercer@quintarion.tech</span>
        </div>
        <div class="contact">
          <svg viewBox="0 0 24 24" aria-hidden="true"><path d="M12 2a10 10 0 1 0 0 20 10 10 0 0 0 0-20zm-1 17.9A8 8 0 0 1 4.2 10L9 14.8v1a2 2 0 0 0 2 2v2.1zm6.9-2.5a2 2 0 0 0-1.9-1.4h-1v-3a1 1 0 0 0-1-1H8v-2h2a1 1 0 0 0 1-1V7h2a2 2 0 0 0 2-2v-.4a8 8 0 0 1 2.9 12.8z"/></svg>
          <span>www.quintarion.tech</span>
        </div>
      </div>
    </div>
  </section>

  <section class="card card--back" aria-label="Business card back">
    <div class="brand-back"><span class="brand-square"></span>Quintarion</div>
  </section>
</body>
</html>
```